Design für 3-Monatskalender
Zielgruppe
Hallo, wir benötigen ein Design bzw. fertige Druckdaten für einen 3 Monatskalender mit den Feiertagen aus DE, AT und CH.
Format ist DIN A6, der Kalender wird benötigt für das Jahr 2024 und 2025.
Aufgabenstellung
Format: DIN A6
Kalendarium 2024 und 2025
Feiertage aus DE, AT und CH
Beispiel anbei, wichtig ist, das wir einen Magnetischen Ring als Datumsschieber nehmen. Der Ring hat die Maße: Durchmesser = 12mm Innendruchmesser = 10mm

```html
<!DOCTYPE html>
<html lang="de">
<head>
<meta charset="utf-8">
<title>3-Monatskalender 2024</title>
<link rel="stylesheet" href="https://fonts.googleapis.com/css2?family=Montserrat:ital,wght@0,400;0,500;0,700;1,400&family=Josefin+Sans:wght@100&display=swap">
<style>
  :root{
    --page:#f3f3f7;
    --ink:#1e1e1e;
    --muted:#6a6a6a;
    --holiday:#c4161c;
    --ring:#c0504a;
    --band-a:#dbdadf;
    --apple-light:#9ccb4e;
    --apple-mid:#7fb83a;
    --apple-dark:#3f7d1c;
  }
  *{box-sizing:border-box;margin:0;padding:0}
  html,body{width:1200px;height:1200px;overflow:hidden;background:var(--page)}
  body{font-family:"Montserrat",sans-serif;color:var(--ink);position:relative}

  .calendar{
    position:absolute;left:259px;top:39px;
    width:852px;height:1402px;
    transform:scale(0.8);transform-origin:0 0;
    background:var(--band-a);
  }

  .cover{position:relative;height:411px;overflow:hidden}
  .cover-photo{
    position:absolute;inset:0;
    background:linear-gradient(160deg, var(--apple-light), var(--apple-mid) 50%, var(--apple-dark));
  }
  .cover-year{position:absolute;inset:0}

  .month{position:relative}
  .month--dec{height:333px;background:linear-gradient(90deg,#dedde2,#d6d5da 70%,#dcdbe0)}
  .month--jan{height:326px;background:linear-gradient(90deg,#efeff2,#e2e1e5 60%,#efeff1)}
  .month--feb{height:332px;background:linear-gradient(90deg,#dedde2,#d3d2d7 70%,#d9d8dd)}

  .year{position:absolute;right:752px;font-weight:700;font-size:31px;line-height:1}
  .week-label{position:absolute;right:752px;text-align:right;font-style:italic;font-size:12.5px;line-height:13px}
  .title{position:absolute;font-weight:700;font-size:31px;line-height:1;white-space:nowrap}

  .weekdays{position:absolute;left:0;display:grid;
    grid-template-columns:102px 171px 87px 90px 85px 85px 90px 86px}
  .weekdays span{text-align:right;font-style:italic;font-size:12px;line-height:13px;white-space:pre}

  .days{position:absolute;left:0;display:grid;
    grid-template-columns:102px 171px 87px 90px 85px 85px 90px 86px;
    grid-auto-rows:45px;align-items:center}
  .days span{position:relative;text-align:right;font-size:36px;line-height:1}
  .days .wk{color:var(--muted)}
  .days .sat{color:var(--muted)}
  .days .hol{color:var(--holiday)}
  .tag{position:absolute;left:100%;top:-4px;margin-left:10px;color:var(--holiday);
    font-style:italic;font-size:10px;line-height:11px;text-align:left}
  .tag--single{top:-2px}
  .ring{position:absolute;width:70px;height:70px;border:5px solid var(--ring);border-radius:50%;
    right:-6px;top:50%;transform:translateY(-50%)}
</style>
</head>
<body>
<main class="calendar">

  <header class="cover">
    <div class="cover-photo" role="img" aria-label="Foto: grüne Äpfel mit einem roten Apfel in der Mitte"></div>
    <svg class="cover-year" viewBox="0 0 852 411" aria-hidden="true">
      <text x="100" y="360" font-family="Josefin Sans, sans-serif" font-weight="100" font-size="360"
            fill="none" stroke="#ffffff" stroke-width="2.5" letter-spacing="-28">2024</text>
    </svg>
  </header>

  <section class="month month--dec">
    <div class="year" style="top:30px">2023</div>
    <div class="week-label" style="top:64px">Woche<br>Week<br>Semaine</div>
    <div class="title" style="left:188px;top:30px">Dezember</div>
    <div class="title" style="left:401px;top:30px">December</div>
    <div class="title" style="left:614px;top:30px">Décembre</div>
    <div class="weekdays" style="top:66px">
      <span></span><span>Montag
Monday
Lundi</span><span>Dienstag
Tuesday
Mardi</span><span>Mittwoch
Wednesday
Mercredi</span><span>Donnerstag
Thursday
Jeudi</span><span>Freitag
Friday
Vendredi</span><span>Samstag
Saturday
Samedi</span><span>Sonntag
Sunday
Dimanche</span>
    </div>
    <div class="days" style="top:112px">
      <span class="wk">48</span><span></span><span></span><span></span><span></span><span>1</span><span class="sat">2</span><span class="hol">3</span>
      <span class="wk">49</span><span>4</span><span>5</span><span>6</span><span>7</span><span class="hol">8<i class="tag tag--single">AT</i></span><span class="sat">9</span><span class="hol">10</span>
      <span class="wk">50</span><span>11</span><span>12</span><span>13</span><span>14</span><span>15</span><span class="sat">16</span><span class="hol">17</span>
      <span class="wk">51</span><span>18</span><span>19</span><span>20</span><span>21</span><span>22</span><span class="sat">23</span><span class="hol">24</span>
      <span class="wk">52</span><span class="hol">25<i class="tag">AT<br>DE<br>CH</i></span><span class="hol">26<i class="tag">AT<br>DE<br>CH</i></span><span>27</span><span>28</span><span>29</span><span></span><span class="hol">31</span>
    </div>
  </section>

  <section class="month month--jan">
    <div class="year" style="top:17px">2024</div>
    <div class="week-label" style="top:51px">Woche<br>Week<br>Semaine</div>
    <div class="title" style="left:187px;top:17px">Januar</div>
    <div class="title" style="left:347px;top:17px">January</div>
    <div class="title" style="left:526px;top:17px">Janvier</div>
    <div class="weekdays" style="top:52px">
      <span></span><span>Montag
Monday
Lundi</span><span>Dienstag
Tuesday
Mardi</span><span>Mittwoch
Wednesday
Mercredi</span><span>Donnerstag
Thursday
Jeudi</span><span>Freitag
Friday
Vendredi</span><span>Samstag
Saturday
Samedi</span><span>Sonntag
Sunday
Dimanche</span>
    </div>
    <div class="days" style="top:97px">
      <span class="wk">1</span><span class="hol">1<i class="tag">AT<br>DE<br>CH</i></span><span>2</span><span>3</span><span>4</span><span>5</span><span class="sat">6</span><span class="hol">7</span>
      <span class="wk">2</span><span>8</span><span>9</span><span>10</span><span>11</span><span>12</span><span class="sat">13</span><span class="hol">14</span>
      <span class="wk">3</span><span>15</span><span>16</span><span>17</span><span>18</span><span>19</span><span class="sat">20</span><span class="hol">21</span>
      <span class="wk">4</span><span>22</span><span>23</span><span>24<i class="ring"></i></span><span>25</span><span>26</span><span class="sat">27</span><span class="hol">28</span>
      <span class="wk">5</span><span>29</span><span>30</span><span>31</span><span></span><span></span><span></span><span></span>
    </div>
  </section>

  <section class="month month--feb">
    <div class="year" style="top:10px">2024</div>
    <div class="week-label" style="top:45px">Woche<br>Week<br>Semaine</div>
    <div class="title" style="left:186px;top:10px">Februar</div>
    <div class="title" style="left:362px;top:10px">February</div>
    <div class="title" style="left:548px;top:10px">Février</div>
    <div class="weekdays" style="top:45px">
      <span></span><span>Montag
Monday
Lundi</span><span>Dienstag
Tuesday
Mardi</span><span>Mittwoch
Wednessday
Mercredi</span><span>Donnersatg
Thursday
Jeudi</span><span>Freitag
Friday
Ventredi</span><span>Samstag
Saturday
Samedi</span><span>Sonntag
Sunday
Dimanche</span>
    </div>
    <div class="days" style="top:93px">
      <span class="wk">5</span><span></span><span></span><span></span><span>1</span><span>2</span><span class="sat">3</span><span class="hol">4</span>
      <span class="wk">6</span><span>5</span><span>6</span><span>7</span><span>8</span><span>9</span><span class="sat">10</span><span class="hol">11</span>
      <span class="wk">7</span><span>12</span><span>13</span><span>14</span><span>15</span><span>16</span><span class="sat">17</span><span class="hol">18</span>
      <span class="wk">8</span><span>19</span><span>20</span><span>21</span><span>22</span><span>23</span><span class="sat">24</span><span class="hol">25</span>
      <span class="wk">9</span><span>26</span><span>27</span><span>28</span><span>29</span><span></span><span></span><span></span>
    </div>
  </section>

</main>
</body>
</html>
```